We are looking for a new PowerPoint template for our new CI

Hey artmingle! For 25 years we have been an owner-managed IT system house with tradition, values and a great team. After more than 10 years, we would like to upgrade our company and design the entire CI contemporary and modern. Therefore we are looking for a Powerpoint Template which fits to our logo, the colors and an IT company. Details about our company and our service portfolio can be found on our homepage. We are currently adapting our homepage to the new CI resulting from the logo revision. Homepage: http://stage.kovantra.de Color codes: Gray = RGB: 4040404040 White = RGB: F5F5F5F5F5 Orange = RGB: F7931E Our slogan: We keep your system running Our address data: Company = Kovantra GmbH Street = Lindbergstraße 12 POSTCODE = 71844 City = Hollbach We look forward to your ideas and thank you all in advance.

Target Market(s)

Our target group are companies with 10 to 100 employees from all industrial sectors, eg https://www.morvik-werke.de/ https://www.faltner-logistik.de/ https://www.quensel.de/ de /

Colors

Designer to choose colors to be used in the design.

Requirements
Must have
• We are looking for a modern IT design in gray / orange. The basis of the design should be our logo. The template should have two different layouts and three different layouts for content. Our logo and slogan should be clearly visible on the start layout. In addition, an area should be reserved for the name of a speaker and the occasion of the presentation.

```html
<!DOCTYPE html>
<html lang="de">
<head>
<meta charset="utf-8">
<title>Kovantra – Präsentationsvorlage</title>
<link rel="stylesheet" href="https://fonts.googleapis.com/css2?family=Saira:wght@400;500;600;700&display=swap">
<style>
  :root {
    --orange: #f7931e;
    --gray: #404040;
    --gray-mid: #4a4a4a;
    --white: #f5f5f5;
    --paper: #ffffff;
    --footer-light: #ececec;
    --text-dark: #333333;
  }
  * { box-sizing: border-box; margin: 0; padding: 0; }
  html, body { width: 1200px; height: 1200px; overflow: hidden; background: #fff; }
  body { position: relative; font-family: "Saira", sans-serif; color: var(--text-dark); }
  h1, h2 { font-weight: 400; }

  .slide { position: absolute; width: 597px; height: 336px; overflow: hidden; }
  .slide--cover    { left: 5px;   top: 64px; }
  .slide--about    { left: 605px; top: 64px; }
  .slide--services { left: 5px;   top: 416px; }
  .slide--team     { left: 605px; top: 416px; }
  .slide--prices   { left: 304px; top: 779px; }

  .footer {
    position: absolute; left: 0; bottom: 0; width: 100%; height: 35px;
    display: flex; align-items: center; justify-content: space-between;
    padding: 0 42px 0 46px; background: var(--footer-light);
    font-size: 10px; letter-spacing: 0.4px; color: var(--text-dark);
  }
  .footer--orange { background: var(--orange); color: #fff; }
  .brand { display: flex; align-items: center; gap: 6px; font-weight: 700; font-size: 16px; letter-spacing: 1px; color: var(--gray); }
  .brand__dot { width: 9px; height: 9px; border-radius: 50%; background: currentColor; }
  .footer--orange .brand { color: #fff; }

  .photo { position: absolute; }

  /* cover */
  .cover__bg { inset: 0 0 35px 0; background: radial-gradient(ellipse at 62% 40%, #3c3f42 0%, #232527 55%, #151617 100%); }
  .slogan { position: absolute; left: 45px; top: 47px; font-weight: 400; }
  .slogan__line { display: block; width: max-content; height: 39px; margin-bottom: 7px; padding: 0 12px; font-size: 31px; line-height: 38px; color: #fff; background: var(--orange); }
  .slogan__line--muted { background: #8a8a8a; }
  .speaker { position: absolute; left: 42px; top: 241px; font-size: 14px; color: #fff; }
  .speaker__label { color: #9a9a9a; font-weight: 600; margin-right: 4px; }

  /* about */
  .slide--about { background: var(--gray); }
  .about__title { position: absolute; left: 0; top: 9px; width: 206px; height: 39px; background: var(--orange); color: #fff; font-size: 24px; line-height: 39px; padding-left: 33px; }
  .about__box { position: absolute; left: 21px; top: 58px; width: 318px; height: 202px; background: var(--white); padding: 22px 26px 0 31px; font-size: 11px; line-height: 17.5px; color: #222; }
  .about__box strong { display: block; font-weight: 700; margin-bottom: 14px; }
  .about__pointer { position: absolute; left: 73px; top: 259px; }

  /* services */
  .services__bg { inset: 0 0 35px 0; background: linear-gradient(90deg, #1f1f1f, #2c2c2c 50%, #1f1f1f); }
  .services__title { position: absolute; top: 14px; width: 100%; text-align: center; font-size: 22px; line-height: 26px; color: #fff; }
  .hub { position: absolute; left: 181px; top: 89px; width: 235px; height: 153px; background: var(--orange); display: flex; align-items: center; justify-content: center; }
  .hub .brand { color: #fff; font-size: 24px; }
  .hub .brand__dot { width: 13px; height: 13px; }
  .service { position: absolute; width: 107px; height: 42px; background: var(--paper); font-size: 8.5px; line-height: 11px; text-align: center; padding-top: 9px; color: var(--text-dark); }
  .service--left { left: 74px; }
  .service--right { left: 416px; }
  .service--bottom { left: 233px; top: 243px; width: 132px; padding-top: 10px; }
  .service::after { content: ""; position: absolute; width: 0; height: 0; border: 4px solid transparent; }
  .service--left::after { right: -8px; top: 17px; border-left-color: var(--paper); }
  .service--right::after { left: -8px; top: 17px; border-right-color: var(--paper); }
  .service--bottom::after { top: -8px; left: 62px; border-bottom-color: var(--paper); }

  /* team */
  .slide--team { background: var(--gray-mid); }
  .team__aside { position: absolute; left: 0; top: 0; width: 178px; height: 301px; background: var(--gray); }
  .team__title { position: absolute; left: 0; top: 0; width: 178px; height: 67px; background: var(--orange); color: #fff; font-size: 24px; padding: 18px 0 0 21px; }
  .team__title::after { content: ""; position: absolute; left: 22px; bottom: -7px; border: 7px solid transparent; border-bottom: 0; border-top-color: var(--orange); }
  .team__facts-title { position: absolute; left: 21px; top: 82px; color: #fff; font-size: 16px; line-height: 19px; }
  .fact { position: absolute; left: 21px; display: flex; align-items: center; color: #fff; font-size: 7px; }
  .fact__num { color: var(--orange); font-weight: 700; font-size: 24px; margin-right: 5px; }
  .fact__sep { width: 1px; height: 12px; background: #fff; margin-right: 7px; }
  .member { position: absolute; width: 96px; margin-left: -48px; text-align: center; }
  .member__photo { width: 75px; height: 75px; margin: 0 auto; border-radius: 50%; border: 3px solid var(--orange); background: radial-gradient(circle at 50% 40%, #e9ecef, #b9c1c8); }
  .member__photo--pets { background: radial-gradient(circle at 50% 55%, #c79a5c, #8b6a45); }
  .member__name { margin-top: 10px; color: var(--orange); font-size: 9.5px; }
  .member__role { color: #fff; font-size: 6px; line-height: 9px; }

  /* prices */
  .prices__bg { inset: 0 0 35px 0; }
  .prices__title { position: absolute; top: 20px; width: 100%; text-align: center; color: #fff; font-size: 22px; }
  .prices__title span { color: var(--orange); }
  .price { position: absolute; top: 83px; width: 144px; height: 194px; background: var(--paper); text-align: center; box-shadow: 0 2px 8px rgba(0,0,0,.12); }
  .price::before { content: ""; position: absolute; left: 62px; top: 0; border: 10px solid transparent; border-bottom: 0; border-top-color: var(--orange); }
  .price::after { content: ""; position: absolute; left: 41px; bottom: 0; width: 62px; height: 3px; background: var(--orange); }
  .price__label { margin-top: 20px; font-size: 11px; color: #222; }
  .price__amount { color: var(--orange); font-weight: 700; font-size: 30px; line-height: 30px; margin-top: 3px; }
  .price__unit { color: var(--orange); font-size: 15px; line-height: 15px; }
  .price__text { margin: 19px 14px 0; font-size: 7.3px; line-height: 11.7px; color: #444; }
</style>
</head>
<body>

<!-- Cover -->
<section class="slide slide--cover">
  <div class="photo cover__bg" role="img" aria-label="Dunkles Foto eines Rechenzentrums mit Techniker am Laptop zwischen Serverschränken"></div>
  <h1 class="slogan">
    <span class="slogan__line">We keep</span>
    <span class="slogan__line">your system</span>
    <span class="slogan__line slogan__line--muted">running</span>
  </h1>
  <p class="speaker"><span class="speaker__label">SPEAKER</span> | Tobias Kessler</p>
  <footer class="footer">
    <span class="brand"><span class="brand__dot"></span>KOVANTRA</span>
    <span>Kovantra GmbH | Lindbergstraße 12 | 71844 Hollbach</span>
  </footer>
</section>

<!-- About -->
<section class="slide slide--about">
  <svg class="photo" width="597" height="301" style="left:0;top:0" role="img" aria-label="Porträtfoto der beiden Geschäftsführer in hellen Hemden">
    <defs><linearGradient id="aboutPhoto" x1="0" x2="1"><stop offset="0" stop-color="#c9cfd3"/><stop offset="1" stop-color="#e7e9ea"/></linearGradient></defs>
    <polygon points="342,0 597,0 597,301 324,301" fill="url(#aboutPhoto)"/>
    <polygon points="331,0 342,0 324,301 313,301" fill="var(--orange)"/>
  </svg>
  <h2 class="about__title">Wer sind wir?</h2>
  <div class="about__box">
    <strong>Wir sind seit 25 Jahren ein inhabergeführtes Familienunternehmen mit Traditionen, Werten und einem ganz tollen Team.</strong>
    Wir legen großen Wert auf Menschlichkeit, langjährige Partnerschaften und Arbeiten auf Augenhöhe. Wir lieben unsere Arbeit, sind für unsere Mitarbeiter da und bewegen Berge für unsere Kunden.
  </div>
  <svg class="about__pointer" width="44" height="21" aria-hidden="true"><polygon points="0,0 44,0 22,21" fill="var(--white)"/></svg>
  <footer class="footer footer--orange">
    <span class="brand"><span class="brand__dot"></span>KOVANTRA</span>
    <span>Kovantra GmbH | Lindbergstraße 12 | 71844 Hollbach</span>
  </footer>
</section>

<!-- Services -->
<section class="slide slide--services">
  <div class="photo services__bg" role="img" aria-label="Abgedunkeltes Foto von Serverreihen"></div>
  <h2 class="services__title">Produkte und Leistungen unseres<br>IT Systemhauses</h2>
  <div class="hub"><span class="brand"><span class="brand__dot"></span>KOVANTRA</span></div>
  <div class="service service--left" style="top:73px">Corvana Medica Die<br>Praxissoftware</div>
  <div class="service service--left" style="top:124px">Hardware und<br>Software</div>
  <div class="service service--left" style="top:175px">Service vor Ort</div>
  <div class="service service--left" style="top:226px">IT Management</div>
  <div class="service service--right" style="top:73px">Hochleistungs<br>Firewalls und VPN</div>
  <div class="service service--right" style="top:124px">Kovantra Managed<br>Backup</div>
  <div class="service service--right" style="top:175px">Projektmanagment</div>
  <div class="service service--right" style="top:226px">Hotline und Support</div>
  <div class="service service--bottom">Virtuelle Telefonanlage und<br>VoIP Telefonie</div>
  <footer class="footer">
    <span class="brand"><span class="brand__dot"></span>KOVANTRA</span>
    <span>Kovantra GmbH | Lindbergstraße 12 | 71844 Hollbach</span>
  </footer>
</section>

<!-- Team -->
<section class="slide slide--team">
  <div class="team__aside"></div>
  <h2 class="team__title">Unser Team</h2>
  <p class="team__facts-title">Zahlen und<br>Fakten 2019</p>
  <div class="fact" style="top:140px"><span class="fact__num">560</span><span class="fact__sep"></span>Kundengeräte</div>
  <div class="fact" style="top:170px"><span class="fact__num">3300</span><span class="fact__sep"></span>Tickets</div>
  <div class="fact" style="top:203px"><span class="fact__num">6500</span><span class="fact__sep"></span>Telefonate</div>
  <div class="fact" style="top:236px"><span class="fact__num">220K</span><span class="fact__sep"></span>Zeilen Sourcecode</div>

  <div class="member" style="left:246px;top:27px"><div class="member__photo" role="img" aria-label="Porträtfoto Jonas Brenner"></div><p class="member__name">Jonas Brenner</p><p class="member__role">Founder &amp; CEO</p></div>
  <div class="member" style="left:343px;top:29px"><div class="member__photo" role="img" aria-label="Porträtfoto Lukas Brenner"></div><p class="member__name">Lukas Brenner</p><p class="member__role">Head of Sales Department and<br>Officer with Procurement</p></div>
  <div class="member" style="left:440px;top:29px"><div class="member__photo" role="img" aria-label="Porträtfoto Tobias Kessler"></div><p class="member__name">Tobias Kessler</p><p class="member__role">Head of Systems<br>Management and Support</p></div>
  <div class="member" style="left:537px;top:29px"><div class="member__photo" role="img" aria-label="Porträtfoto Felix Wendt"></div><p class="member__name">Felix Wendt</p><p class="member__role">Developer and Support</p></div>

  <div class="member" style="left:246px;top:163px"><div class="member__photo" role="img" aria-label="Porträtfoto Sabine Roth"></div><p class="member__name">Sabine Roth</p><p class="member__role">Support and<br>Facility Service</p></div>
  <div class="member" style="left:343px;top:163px"><div class="member__photo" role="img" aria-label="Porträtfoto Martin Ebner"></div><p class="member__name">Martin Ebner</p><p class="member__role">External Developer</p></div>
  <div class="member" style="left:440px;top:163px"><div class="member__photo" role="img" aria-label="Porträtfoto Laura Hofmann"></div><p class="member__name">Laura Hofmann</p><p class="member__role">Medical Support</p></div>
  <div class="member" style="left:537px;top:163px"><div class="member__photo member__photo--pets" role="img" aria-label="Foto der beiden Bürohunde auf einer Decke"></div><p class="member__name">Bruno und Kira</p><p class="member__role">Heads of Security<br>Department</p></div>

  <footer class="footer" style="padding-left:23px;padding-right:22px">
    <span class="brand"><span class="brand__dot"></span>KOVANTRA</span>
    <span>Kovantra GmbH | Lindbergstraße 12 | 71844 Hollbach</span>
  </footer>
</section>

<!-- Prices -->
<section class="slide slide--prices">
  <svg class="photo prices__bg" width="597" height="301" style="left:0;top:0" role="img" aria-label="Dunkles, unscharfes Foto von Serverschränken mit hellem Bogen darunter">
    <defs><linearGradient id="pricesDark" x1="0" y1="0" x2="0" y2="1"><stop offset="0" stop-color="#141414"/><stop offset="1" stop-color="#262626"/></linearGradient></defs>
    <rect width="597" height="301" fill="url(#pricesDark)"/>
    <path d="M0,152 Q300,250 597,152 L597,301 L0,301 Z" fill="var(--orange)"/>
    <path d="M0,158 Q300,262 597,158 L597,301 L0,301 Z" fill="var(--white)"/>
  </svg>
  <h2 class="prices__title">Unsere Preise für <span>Service und Support</span></h2>
  <div class="price" style="left:68px">
    <p class="price__label">Fahrtkosten</p>
    <p class="price__amount">0,80</p>
    <p class="price__unit">cents</p>
    <p class="price__text">Je gefahrener KM. Unsere Techniker fahren mit einem Service-Fahrzeug zu Ihnen welches mit alle gängigen Ersatzteilen und Produkten ausgestattet ist.</p>
  </div>
  <div class="price" style="left:226px">
    <p class="price__label">Service-Einsatz</p>
    <p class="price__amount">21,25</p>
    <p class="price__unit">euro</p>
    <p class="price__text">Je angefangene 1/4 Stunde für einen Service-Techniker oder Administrator.</p>
  </div>
  <div class="price" style="left:384px">
    <p class="price__label">Fernwartung</p>
    <p class="price__amount">1,42</p>
    <p class="price__unit">euro</p>
    <p class="price__text">je angefangene Minute<br>Technik-Support oder Fernwartungssitzung. Die Abrechnung erfolgt über eine monatliche Sammelrechnung der erbrachten Leistungen.</p>
  </div>
  <footer class="footer footer--orange">
    <span class="brand"><span class="brand__dot"></span>KOVANTRA</span>
    <span>Kovantra GmbH | Lindbergstraße 12 | 71844 Hollbach</span>
  </footer>
</section>

</body>
</html>
```